Tick Tock Green Frog

I'm looking for one generic business card that be used for four people or would it be easier to get four different design of cards.

I have attached the logo, of the cow. I would also like to use one colour of the cow's legs in the background.

Info for card:
Dana Holcroft
Keeper of Possibilities
Phone: 044 718 2094
email: dana.holcroft@ticktockgreenfrogs.com.au
Web: www.ticktockgreenfrogs.com.au

Here is some tag lines that could also be used:

"Guiding you toward the right path"

"Bringing the joy back to early learning"
"Where there is NO fuss"

Industry/Entity Type

Business

```html
<!DOCTYPE html>
<html lang="en">
<head>
<meta charset="utf-8">
<title>Tick Tock Green Frog – Business Card</title>
<link rel="stylesheet" href="https://fonts.googleapis.com/css2?family=Open+Sans:wght@400;600&family=Crimson+Text:ital,wght@1,700&display=swap">
<style>
  :root {
    --page: #ecebe8;
    --card-white: #ffffff;
    --card-grey: #e6e6e6;
    --green: #4f9a34;
    --green-dark: #1e7a33;
    --green-deep: #16702c;
    --green-glow: #3fae3f;
    --ink: #222222;
    --ink-soft: #8a8a8a;
    --brown: #4a2a12;
    --white: #ffffff;
  }
  * { box-sizing: border-box; margin: 0; padding: 0; }
  html, body { width: 1200px; height: 1024px; overflow: hidden; }
  body {
    background: var(--page);
    font-family: "Open Sans", Arial, sans-serif;
    position: relative;
  }
  .card {
    position: absolute;
    width: 680px;
    height: 400px;
    border-radius: 22px;
    overflow: hidden;
    box-shadow: 0 6px 18px rgba(0,0,0,.18);
  }
  .card--front {
    left: 90px; top: 70px;
    background: radial-gradient(ellipse at 45% 45%, var(--card-white) 0%, var(--card-white) 40%, var(--card-grey) 100%);
  }
  .brand {
    position: absolute;
    left: 0; right: 0;
    display: flex; align-items: center; justify-content: center; gap: 10px;
    color: var(--brown);
    font-weight: 600;
  }
  .card--front .brand { top: 140px; font-size: 24px; }
  .brand__mark { width: 14px; height: 14px; background: var(--green); }
  .band {
    position: absolute;
    background: linear-gradient(90deg, var(--green) 0%, var(--green-dark) 100%);
  }
  .band--tagline {
    left: 50%; right: 0; top: 208px;
    height: 24px;
    color: var(--white);
    font-size: 13px;
    line-height: 24px;
    padding-left: 18px;
  }
  .band--name { left: 0; width: 160px; top: 285px; height: 20px; background: linear-gradient(90deg, var(--green-dark), var(--green)); }
  .person { position: absolute; left: 170px; top: 258px; }
  .person__name {
    font-family: "Crimson Text", Georgia, serif;
    font-style: italic; font-weight: 700;
    font-size: 30px; color: var(--ink); line-height: 1;
  }
  .person__role { font-size: 12px; color: var(--ink-soft); margin-top: 2px; }
  .contacts {
    position: absolute; left: 168px; top: 314px;
    list-style: none; font-size: 12px; color: var(--ink);
  }
  .contacts__item { display: flex; align-items: center; gap: 10px; height: 22px; }
  .contacts__icon { width: 16px; height: 16px; flex: none; }

  .card--back {
    left: 430px; top: 560px;
    background: radial-gradient(ellipse at 48% 38%, var(--green-glow) 0%, var(--green-dark) 55%, var(--green-deep) 100%);
    color: var(--white);
    text-align: center;
  }
  .card--back .brand { top: 130px; font-size: 26px; }
  .taglines { position: absolute; left: 0; right: 0; top: 196px; }
  .taglines__lead { font-size: 22px; line-height: 1.1; }
  .taglines__line { font-size: 16px; line-height: 1.15; }
  .taglines__small { font-size: 13px; line-height: 1.3; }
  .card--back .web { position: absolute; left: 0; right: 0; top: 316px; font-size: 10px; }
</style>
</head>
<body>

<section class="card card--front" aria-label="Business card front">
  <div class="brand"><span class="brand__mark"></span>Tick Tock Green Frog</div>
  <div class="band band--tagline">Guiding you toward the right path</div>
  <div class="band band--name"></div>
  <div class="person">
    <p class="person__name">Dana Holcroft</p>
    <p class="person__role">Keeper of Possibilities</p>
  </div>
  <ul class="contacts">
    <li class="contacts__item">
      <svg class="contacts__icon" viewBox="0 0 16 16" aria-hidden="true"><circle cx="8" cy="8" r="7.5" fill="#1e7a33"/><path d="M5.2 4.2l1.6-.3.8 2-1 .8a5 5 0 0 0 2.7 2.7l.8-1 2 .8-.3 1.6c-3.6.3-6.9-3-6.6-6.6z" fill="#fff"/></svg>
      044 718 2094
    </li>
    <li class="contacts__item">
      <svg class="contacts__icon" viewBox="0 0 16 16" aria-hidden="true"><circle cx="8" cy="8" r="7.5" fill="#1e7a33"/><rect x="4" y="5.2" width="8" height="5.6" fill="none" stroke="#fff" stroke-width="1"/><path d="M4 5.2l4 3 4-3" fill="none" stroke="#fff" stroke-width="1"/></svg>
      dana.holcroft@ticktockgreenfrogs.com.au
    </li>
    <li class="contacts__item">
      <svg class="contacts__icon" viewBox="0 0 16 16" aria-hidden="true"><circle cx="8" cy="8" r="7.5" fill="#1e7a33"/><circle cx="8" cy="8" r="4.3" fill="none" stroke="#fff" stroke-width="1"/><ellipse cx="8" cy="8" rx="1.8" ry="4.3" fill="none" stroke="#fff" stroke-width="1"/><path d="M3.7 8h8.6" stroke="#fff" stroke-width="1"/></svg>
      www.ticktockgreenfrogs.com.au
    </li>
  </ul>
</section>

<section class="card card--back" aria-label="Business card back">
  <div class="brand"><span class="brand__mark"></span>Tick Tock Green Frog</div>
  <div class="taglines">
    <p class="taglines__lead">Where there is NO fuss</p>
    <p class="taglines__line">Guiding you toward the right path</p>
    <p class="taglines__small">Bringing the joy back to early learning</p>
  </div>
  <p class="web">www.ticktockgreenfrogs.com.au</p>
</section>

</body>
</html>
```